Design the web for "http://www.qlchatter.example"

QLChatter is an open source customer communication platform, think as BRAVOLINK.IO alternative.

QLChatter web site is an entry to let people know QLChatter and try QLChatter online QLChatter service.

1, To design the web site, suggest try QLChatter first.

2, At least replace the original pictures which QLChatter web site now use. (All got from cloudshelf site, shame and not reasonable)

3, Provide total web design, Picture and Code.

Thanks,
QLChatter owner
Haoran Wei
weihaoran@mailbox.example

Reason: So far no useful design, and only five designers submit their designs. And one man submit 48 designs, most of his design is same style. I request to extend the deadline, and invite more designers. Thanks, Haoran

Target Market(s)

Open Source.

Industry/Entity Type

Software

Coding

Coded - Design and coding required

Number of Pages Required

2 page

Font styles to use
Sans Serif

Requirements
Must have
• 1) Try QLChatter first
• 2) Replace all the pictures in the current site.
• 3) Match with the QLChattr features (Customer Communication / Open Source / Open API etc.)
• 4) Download page presents QLChatter support all kinds of platforms since QLChatter has all kinds of application for different OS.
• 5) Web style tuning (The current style copy from cloudshelf)
• 6) All pictures and web code.
Nice to have
• 1) Logo tuning for the new web style and logo file attached.
• 2) Extremely simple style is prefer.

```html
<!DOCTYPE html>
<html lang="en">
<head>
<meta charset="utf-8">
<title>QLChatter – Documentation</title>
<link rel="stylesheet" href="https://fonts.googleapis.com/css2?family=Open+Sans:wght@400;600;700&display=swap">
<style>
  :root{
    --ink:#333;
    --ink-soft:#777;
    --muted:#888;
    --accent:#3a87c8;
    --brand:#52c3d6;
    --rule:#c9c9c9;
    --button:#3b7fc4;
    --tile-blue:#3b8ff0;
    --tile-green:#1fa463;
    --tile-warm:#f39a2a;
    --tile-red:#e2532f;
  }
  *{box-sizing:border-box;margin:0;padding:0}
  html,body{width:1200px;height:1000px;overflow:hidden;background:#fff}
  body{font-family:"Open Sans",sans-serif;color:var(--ink);position:relative}

  .site-header{position:absolute;left:72px;top:50px;width:1042px;height:70px}
  .brand{position:absolute;left:3px;top:3px;display:flex;align-items:center;gap:16px}
  .brand-mark{width:58px;height:58px;border-radius:6px;background:var(--brand)}
  .brand-name{font-size:42px;font-weight:600;color:var(--brand);letter-spacing:-.5px;line-height:1}
  .account{position:absolute;right:2px;top:2px;display:flex;align-items:center;gap:16px;font-size:19px;color:var(--muted)}
  .mail{position:relative;width:30px;height:26px}
  .mail .badge{position:absolute;left:-8px;top:-6px;width:18px;height:18px;border-radius:50%;background:#23b9cc;color:#fff;font-size:11px;font-weight:700;text-align:center;line-height:18px}
  .main-nav{position:absolute;right:0;top:44px;display:flex;gap:24px;align-items:center;font-size:19px;font-weight:600}
  .main-nav a{color:var(--ink);text-decoration:none}
  .main-nav a.current{color:var(--accent)}

  .page-title{position:absolute;left:73px;top:158px;font-size:25px;font-weight:400;color:var(--ink)}
  .title-rule{position:absolute;left:72px;top:198px;width:1043px;border-top:1px solid var(--rule)}
  .breadcrumb{position:absolute;left:73px;top:204px;font-size:13.5px;color:var(--muted);display:flex;gap:12px;align-items:center}
  .breadcrumb a{color:var(--accent);text-decoration:none;font-weight:600}
  .breadcrumb .sep{font-size:9px}

  .hero{position:absolute;left:72px;top:250px;width:1049px;height:333px;overflow:hidden}
  .hero-photo{position:absolute;inset:0;background:
      radial-gradient(ellipse at 85% 40%,#b9b6b0 0,#b9b6b0 8%,transparent 22%),
      radial-gradient(ellipse at 20% 55%,#9c9a94 0,transparent 45%),
      linear-gradient(100deg,#4b4036 0%,#5d5046 45%,#4a3d33 100%)}
  .hero h1{position:absolute;left:42px;top:32px;font-size:48px;font-weight:600;color:#fff;line-height:64px;text-shadow:0 2px 4px rgba(0,0,0,.45);white-space:nowrap}
  .hero .cta{position:absolute;left:42px;top:236px;width:227px;height:52px;background:var(--button);color:#fff;font-size:26px;font-weight:600;line-height:52px;text-align:center;text-decoration:none}

  .format-art{position:absolute;left:72px;top:611px;width:361px;height:299px;
    background:linear-gradient(135deg,var(--tile-blue) 0%,var(--tile-green) 35%,var(--tile-warm) 70%,var(--tile-red) 100%);
    opacity:.85}

  .features{position:absolute;left:492px;top:608px;width:640px}
  .features h2{font-size:25px;font-weight:400;color:var(--ink-soft);margin-bottom:10px;white-space:nowrap;letter-spacing:.1px}
  .features h3{font-size:21px;font-weight:400;color:var(--accent);margin:0 0 14px 1px}
  .features h3.second{margin:0 0 4px 3px}
  .features ul{list-style:none;margin:0 0 2px 26px;font-size:18.5px;line-height:25.5px;color:var(--ink)}
  .features li{position:relative;padding-left:17px}
  .features li::before{content:"";position:absolute;left:0;top:10px;width:8px;height:8px;border-radius:50%;background:#888}

  .site-footer{position:absolute;left:74px;top:942px;width:1040px;border-top:1px solid var(--rule);padding-top:11px;display:flex;justify-content:space-between;font-size:16px}
  .site-footer .copy{color:var(--muted);font-weight:600}
  .site-footer nav{display:flex;gap:22px;font-weight:600}
  .site-footer nav a{color:var(--ink);text-decoration:none}
</style>
</head>
<body>
<header class="site-header">
  <div class="brand">
    <span class="brand-mark"></span>
    <span class="brand-name">qlchatter</span>
  </div>
  <div class="account">
    <span class="mail">
      <svg width="30" height="26" viewBox="0 0 30 26"><rect x="4" y="7" width="22" height="15" fill="#fff" stroke="#777" stroke-width="2"/><path d="M4 7L15 16L26 7" fill="none" stroke="#777" stroke-width="2"/></svg>
      <span class="badge">2</span>
    </span>
    <span>My Account</span>
  </div>
  <nav class="main-nav">
    <a href="#">Home</a>
    <a href="#" class="current">Documentation</a>
    <a href="#">Download</a>
    <a href="#">About Us</a>
    <svg width="20" height="20" viewBox="0 0 20 20" aria-label="Search"><circle cx="12" cy="8" r="6" fill="none" stroke="#333" stroke-width="2"/><path d="M8 12L2 18" stroke="#333" stroke-width="2.4" stroke-linecap="round"/></svg>
  </nav>
</header>

<h1 class="page-title">Documentation</h1>
<div class="title-rule"></div>
<div class="breadcrumb"><a href="#">Documentation</a><span class="sep">▶</span><span>Introduction</span></div>

<section class="hero">
  <div class="hero-photo" role="img" aria-label="Photo of a wooden desk with blueprints, glasses, a clipboard with charts, a laptop and a cup of tea"></div>
  <h1>Open Source Plug &amp; Play<br>Customer Communication Platform</h1>
  <a href="#" class="cta">Download Now</a>
</section>

<div class="format-art" role="img" aria-label="Illustration of twelve coloured file-type icons in a four by three grid"></div>

<section class="features">
  <h2>Easy Integration and support for all kinds of platforms</h2>
  <h3>All kinds of platforms</h3>
  <ul>
    <li>QLChatter backend run on Fenestra, Orchard OS, Penguix</li>
    <li>QLChatter service-end run on Fenestra, Orchard OS, Penguix, Robodroid, PocketOS, &nbsp;Fenestra Mobile</li>
    <li>QLChatter customer-end run on Web, PocketOS and Robodroid</li>
  </ul>
  <h3 class="second">Easy to use</h3>
  <ul>
    <li>One line code integrate in customer-end</li>
    <li>One command to deploy QLChatter</li>
    <li>One directive integrate with manager user interface</li>
  </ul>
</section>

<footer class="site-footer">
  <span class="copy">© 2016 | QLChatter.&nbsp; All rights reserved.</span>
  <nav><a href="#">FAQ</a><a href="#">Legal</a><a href="#">Contact</a></nav>
</footer>
</body>
</html>
```